Need a redesign for our Wordpress Credit report website

Hi, We need someone to redesign our Wordpress credit report website, brightledgerview.co.za. The designer will be responsible for the following pages:
- home page
- blog page
- single post
- dashboard
- credit report page

About BrightLedgerView.co.za
Bright Ledger View is a consumer focussed credit report platform where South African citizens can get an easy to understand credit report that shows them where to improve their credit scores.

```html
<!DOCTYPE html>
<html lang="en">
<head>
<meta charset="utf-8">
<title>Bright Ledger View — Home</title>
<link href="https://fonts.googleapis.com/css2?family=Poppins:ital,wght@0,300;0,400;0,500;0,600;0,700;1,400&family=Montserrat:wght@800&display=swap" rel="stylesheet">
<style>
:root{
  --blue:#1f6fc9;
  --blue-dark:#1a5aa8;
  --green:#8cc63f;
  --ink:#333a44;
  --muted:#7b8591;
  --line:#d7dde4;
  --paper:#ffffff;
  --soft:#f3f4f6;
}
*{box-sizing:border-box;margin:0;padding:0}
html,body{width:1200px;height:4894px;overflow:hidden}
body{position:relative;background:var(--paper);font-family:'Poppins',sans-serif;color:var(--ink)}
.abs{position:absolute}
.brand{display:flex;align-items:center;gap:10px;font-family:'Poppins',sans-serif;font-weight:500;color:var(--blue);font-size:24px;white-space:nowrap}
.brand .dot{width:34px;height:34px;border-radius:50%;background:var(--green);flex:none}

/* header */
.site-header{left:0;top:0;width:1200px;height:92px;background:#fff}
.site-header .brand{position:absolute;left:133px;top:28px}
.nav{position:absolute;left:612px;top:34px;display:flex;gap:28px;font-size:13px;font-weight:500}
.nav a{color:var(--ink);text-decoration:none}
.nav a.active{color:var(--blue)}
.pill{position:absolute;top:30px;height:32px;border-radius:16px;color:#fff;font-size:12px;font-weight:600;display:flex;align-items:center;justify-content:center}
.pill.contact{left:855px;width:118px;background:var(--green)}
.pill.login{left:980px;width:90px;background:var(--blue)}

/* hero */
.hero{left:0;top:92px;width:1200px;height:592px;background:linear-gradient(120deg,#4b5560 0%,#7d8a93 40%,#c3c9cc 70%,#9aa3a8 100%)}
.hero-panel{left:104px;top:218px;width:566px;height:348px;background:rgba(31,111,201,.94);border-radius:26px 26px 170px 26px;padding:24px 52px}
.hero-panel h1{font-family:'Montserrat',sans-serif;font-weight:800;color:#fff;font-size:40px;line-height:47px;margin-top:16px}
.hero-panel p{color:#fff;font-size:15px;line-height:21px;margin-top:16px;width:400px}
.btn-more{display:inline-flex;align-items:center;gap:12px;margin-top:20px;background:#fff;color:var(--blue);border-radius:18px;height:34px;padding:0 14px 0 24px;font-size:11px;font-weight:700}
.slider-dots{left:1137px;top:350px;display:flex;flex-direction:column;gap:8px}
.slider-dots span{width:12px;height:12px;border-radius:50%;border:2px solid #fff}
.slider-dots span.on{background:var(--green);border-color:var(--green)}

/* check */
.devices{left:171px;top:813px;width:418px;height:350px;background:linear-gradient(180deg,#e9edf1,#cfd6dd);border-radius:14px}
.check-card{left:688px;top:756px;width:319px;height:444px;background:#fff;box-shadow:0 4px 18px rgba(0,0,0,.14);border-right:4px solid var(--blue)}
.check-card h2{position:absolute;left:54px;top:30px;color:var(--blue);font-size:27px;font-weight:700}
.check-card h2::after{content:"";position:absolute;left:0;right:0;bottom:-6px;height:2px;background:var(--green)}
.field{position:absolute;left:34px;width:234px;height:42px;border:2px solid #c9d0d8;border-radius:6px;font-size:12px;color:#98a1ab;padding:11px 18px}
.agree{position:absolute;left:34px;top:352px;font-size:10px;color:#98a1ab;display:flex;gap:7px;align-items:center}
.agree i{width:13px;height:13px;border:1.5px solid #98a1ab}
.btn-check{position:absolute;left:76px;top:387px;width:136px;height:34px;border-radius:17px;background:var(--green);color:#fff;font-size:11px;font-weight:700;display:flex;align-items:center;justify-content:space-between;padding:0 6px 0 26px}
.btn-check b{width:26px;height:26px;border-radius:50%;border:2px solid #fff;display:flex;align-items:center;justify-content:center}

/* testimonials */
.section-title{position:absolute;left:0;width:1200px;text-align:center;font-size:38px;font-weight:500;z-index:2}
.section-title::after{content:"";position:absolute;left:562px;top:62px;width:76px;height:3px;background:linear-gradient(90deg,currentColor 0 38%,transparent 38% 48%,currentColor 48%)}
.reviews{left:0;top:1302px;width:1200px;height:575px;background:linear-gradient(90deg,#1e65bd 0%,#2a70c2 45%,#7e8f9f 72%,#a6a39c 100%)}
.review{position:absolute;background:#fff;border:3px solid var(--green);padding:26px 22px}
.review .who{display:flex;gap:14px;align-items:center}
.avatar{width:54px;height:54px;border-radius:50%;background:linear-gradient(#c9b39e,#8c7461);flex:none}
.review h4{font-family:'Times New Roman',serif;font-size:13px;font-weight:700;color:#222}
.review small{display:block;font-size:10px;color:#555}
.stars{color:#f3b61f;font-size:13px;letter-spacing:2px}
.review p{font-size:10.5px;line-height:17px;color:#444;margin-top:22px}
.arrow{position:absolute;top:1618px;color:#fff;font-size:40px;font-weight:300}

/* features */
.features-bg{left:627px;top:2014px;width:760px;height:760px;border-radius:50%;background:var(--soft)}
.circuit{left:0;top:2204px;width:408px;height:238px;background:linear-gradient(90deg,rgba(31,111,201,.05),rgba(31,111,201,.22) 70%,rgba(31,111,201,.05))}
.feat{position:absolute;font-size:19px;color:#4a4f57}

/* why */
.why{left:0;top:2793px;width:1200px;height:676px;background:var(--green)}
.why-art{left:80px;top:2950px;width:380px;height:524px;background:linear-gradient(180deg,#c64b4b 0%,#e3cdb4 55%,#2d67c0 100%);border-radius:40px}
.acc{position:absolute;left:572px;width:498px;background:#fff;font-size:16px;color:#333;padding:14px 24px;display:flex;justify-content:space-between;align-items:center;height:53px}
.acc b{color:var(--blue);font-size:24px;font-weight:400}
.acc-body{position:absolute;left:572px;top:3211px;width:498px;height:171px;background:#fff;padding:18px 24px;font-size:13.5px;line-height:23px;color:#6b7480}

/* payments */
.map{left:260px;top:3500px;width:700px;height:470px;background:radial-gradient(ellipse at center,#eef0f2 0%,#f7f8f9 60%,#fff 100%)}
.pay-name{position:absolute;width:172px;text-align:center;font-size:21px;font-weight:600}

/* testimonials 2 */
.reviews2{left:0;top:3986px;width:1200px;height:574px;background:linear-gradient(180deg,#8f9aa3 0%,#4f7fb8 35%,#1f66c0 100%)}
.r2-panel{left:89px;top:4186px;width:1024px;height:224px;border-radius:14px;background:rgba(40,100,180,.55)}
.bubble{position:absolute;top:4216px;height:103px;background:#fff;border-radius:10px;padding:14px 14px;font-style:italic;font-size:12.5px;line-height:24px;color:#333}
.bubble::after{content:"";position:absolute;left:34px;bottom:-14px;border:14px solid transparent;border-top-color:#fff;border-bottom:0}
.bubble q{position:absolute;right:14px;bottom:6px;color:var(--green);font-size:34px;font-style:normal;font-weight:700;line-height:1}
.bubble q::before,.bubble q::after{content:""}
.r2-who{position:absolute;top:4349px;display:flex;gap:12px;align-items:center;color:#fff;font-size:14px;line-height:17px}
.r2-who .avatar{width:50px;height:50px;border:3px solid #fff}

/* footer */
.site-footer .brand{position:absolute;left:133px;top:4618px;font-size:20px}
.socials{left:133px;top:4706px;display:flex;gap:6px}
.socials span{width:34px;height:34px;border-radius:50%;border:2px solid var(--blue)}
.socials span:nth-child(even){border-color:var(--green)}
.fcol{position:absolute;top:4610px;padding-left:18px;border-left:3px solid var(--green)}
.fcol h5{font-size:15px;font-weight:600;color:#222;letter-spacing:.5px}
.fcol ul{list-style:none;margin-top:14px}
.fcol li{font-size:12px;color:#444;line-height:29px}
.contact-row{display:flex;gap:12px;align-items:center;font-size:10px;color:#666;margin-top:14px;line-height:13px}
.contact-row i{width:30px;height:30px;border-radius:50%;background:var(--green);flex:none;display:flex;align-items:center;justify-content:center}
.copy{left:0;top:4830px;width:1200px;border-top:1px solid var(--line);padding-top:26px;text-align:center;font-size:10px;color:#888}
</style>
</head>
<body>

<header class="site-header abs">
  <div class="brand"><span class="dot"></span>Bright Ledger View</div>
  <nav class="nav"><a class="active" href="#">HOME</a><a href="#">ABOUT US</a><a href="#">ARTICLES</a></nav>
  <a class="pill contact">CONTACT US</a>
  <a class="pill login">LOGIN</a>
</header>

<section class="hero abs" role="img" aria-label="Photo of a team meeting around a white office table"></section>
<div class="hero-panel abs">
  <h1>CHECK YOUR<br>CREDIT SCORE<br>WITHIN SECONDS</h1>
  <p>Lorem ipsum dolor sit amet, consectetur adipiscing elit, sed do eiusmod tempor incididunt ut labore et dolore magna aliqua vel facilisis.</p>
  <span class="btn-more">LEARN MORE <svg width="18" height="14" viewBox="0 0 18 14"><path d="M1 7h15M10 1l6 6-6 6" fill="none" stroke="#1f6fc9" stroke-width="2"/></svg></span>
</div>
<div class="slider-dots abs"><span></span><span class="on"></span><span></span><span></span></div>

<section class="check">
  <div class="devices abs" role="img" aria-label="Desktop and tablet showing a sample credit report with a score gauge"></div>
  <form class="check-card abs">
    <h2>CHECK NOW</h2>
    <div class="field" style="top:89px">Id number</div>
    <div class="field" style="top:141px">First name</div>
    <div class="field" style="top:192px">Last Name</div>
    <div class="field" style="top:243px">Email</div>
    <div class="field" style="top:295px">Mobile</div>
    <div class="agree"><i></i>I agree with the terms and conditions</div>
    <div class="btn-check">CHECK NOW <b><svg width="14" height="10" viewBox="0 0 14 10"><path d="M1 5h11M8 1l4 4-4 4" fill="none" stroke="#fff" stroke-width="1.6"/></svg></b></div>
  </form>
</section>

<section class="reviews abs" role="img" aria-label="Photo of a smiling businessman at a meeting table behind a blue overlay"></section>
<h2 class="section-title" style="top:1366px;color:#fff">TESTIMONIALS</h2>
<span class="arrow" style="left:106px">&#8249;</span>
<span class="arrow" style="left:1078px">&#8250;</span>
<article class="review" style="left:194px;top:1520px;width:272px;height:224px">
  <div class="who"><span class="avatar" role="img" aria-label="Customer portrait"></span><div><h4>DANA MORROW</h4><small>Fairbrook Hills, CA</small><span class="stars">★★★★★</span></div></div>
  <p>Lorem ipsum dolor sit amet, consectetur adipiscing elit. Donec bibendum tincidunt ipsum, sed finibus sem. Phasellus mattis turpis eget enim tempor venenatis. Maecenas vehicula ligula sit</p>
</article>
<article class="review" style="left:488px;top:1470px;width:236px;height:324px">
  <div class="who"><span class="avatar" role="img" aria-label="Customer portrait"></span><div><h4>MARCUS</h4><small>Fairbrook Hills, CA</small><span class="stars">★★★★★</span></div></div>
  <p style="font-style:italic">Lorem ipsum dolor sit amet, consectetur adipiscing elit. Donec bibendum tincidunt ipsum, sed finibus sem. Phasellus mattis turpis eget enim tempor venenatis. Maecenas vehicula ligula sit amet rutrum varius. Pellentesque feugiat, enim at luctus dignissim.</p>
  <div style="text-align:center;color:var(--blue);font-size:32px;font-weight:700;line-height:26px;margin-top:8px">&#8220;</div>
  <div style="text-align:center;font-size:14px;color:#333">02/09/2022</div>
</article>
<article class="review" style="left:747px;top:1520px;width:271px;height:224px">
  <div class="who"><span class="avatar" role="img" aria-label="Customer portrait"></span><div><h4>LENA FARROW</h4><small>Fairbrook Hills, CA</small><span class="stars">★★★★★</span></div></div>
  <p>Lorem ipsum dolor sit amet, consectetur adipiscing elit. Donec bibendum tincidunt ipsum, sed finibus sem. Phasellus mattis turpis eget enim tempor venenatis. Maecenas vehicula ligula sit</p>
</article>

<section class="features">
  <div class="features-bg abs"></div>
  <div class="circuit abs" role="img" aria-label="Decorative blue circuit-board lines"></div>
  <h2 class="section-title" style="top:1944px;color:var(--blue)">SYSTEM FEATURES</h2>
  <svg class="abs" style="left:0;top:0" width="1200" height="2800" viewBox="0 0 1200 2800">
    <circle cx="597" cy="2337" r="205" fill="none" stroke="#c9d0d8" stroke-width="2"/>
    <path d="M597 2132 A205 205 0 0 0 392 2337" fill="none" stroke="#1f6fc9" stroke-width="2.5"/>
    <path d="M392 2337 A205 205 0 0 0 597 2542" fill="none" stroke="#8cc63f" stroke-width="2.5"/>
    <circle cx="597" cy="2337" r="182" fill="#fff" stroke="#eaedf0" stroke-width="10"/>
    <g fill="#8cc63f">
      <circle cx="648" cy="2139" r="13"/><circle cx="724" cy="2185" r="13"/><circle cx="770" cy="2244" r="13"/>
      <circle cx="785" cy="2329" r="13"/><circle cx="770" cy="2415" r="13"/><circle cx="724" cy="2478" r="13"/><circle cx="648" cy="2529" r="13"/>
    </g>
  </svg>
  <div class="brand abs" style="left:470px;top:2314px;font-size:27px"><span class="dot" style="width:40px;height:40px"></span>Bright Ledger View</div>
  <span class="feat" style="left:676px;top:2118px">Dispute generator - easily manage disputes</span>
  <span class="feat" style="left:756px;top:2172px">Budget tool - easily create a budget</span>
  <span class="feat" style="left:802px;top:2231px">Improve your credit score eBook</span>
  <span class="feat" style="left:819px;top:2316px">Personal Budgeting Spreadsheet</span>
  <span class="feat" style="left:802px;top:2402px">Perfect score video course</span>
  <span class="feat" style="left:756px;top:2465px">Personal Finance Video Tutorials</span>
  <span class="feat" style="left:676px;top:2517px">Dedicated 24/7 Support</span>
</section>

<section class="why abs"></section>
<div class="why-art abs" role="img" aria-label="Illustration of a smiling woman leaning on a large blue question mark"></div>
<h2 class="section-title" style="top:2864px;color:#fff">WHY GET YOUR SCORE FROM US?</h2>
<div class="acc" style="top:3017px">We don't abuse your personal information: <b>+</b></div>
<div class="acc" style="top:3084px">We don't abuse your personal information: <b>+</b></div>
<div class="acc" style="top:3150px">We don't abuse your personal information: <b>&minus;</b></div>
<div class="acc-body">Since 2008 we have helped over 300,000 South Africans make sense of their credit reports, so you can rest assured knowing that we have a proven track record and that you are in safe hands with us.</div>

<section class="payments">
  <div class="map abs" role="img" aria-label="Faint grey world map"></div>
  <svg class="abs" style="left:0;top:3560px" width="1200" height="320" viewBox="0 3560 1200 320">
    <line x1="24" y1="3715" x2="1176" y2="3715" stroke="#222" stroke-width="1.5"/>
    <g fill="#222"><circle cx="24" cy="3715" r="5"/><circle cx="1176" cy="3715" r="5"/>
      <circle cx="294" cy="3715" r="5"/><circle cx="348" cy="3715" r="5"/><circle cx="568" cy="3715" r="5"/><circle cx="622" cy="3715" r="5"/><circle cx="843" cy="3715" r="5"/><circle cx="897" cy="3715" r="5"/></g>
    <g fill="#fff" stroke="#222" stroke-width="1.5">
      <circle cx="184" cy="3715" r="106"/><circle cx="458" cy="3715" r="106"/><circle cx="732" cy="3715" r="106"/><circle cx="1007" cy="3715" r="106"/>
    </g>
    <circle cx="184" cy="3715" r="86" fill="#fff" stroke="#1f6fc9" stroke-width="6"/>
    <circle cx="458" cy="3715" r="86" fill="#fff" stroke="#8cc63f" stroke-width="6"/>
    <circle cx="732" cy="3715" r="86" fill="#fff" stroke="#1f6fc9" stroke-width="6"/>
    <circle cx="1007" cy="3715" r="86" fill="#fff" stroke="#8cc63f" stroke-width="6"/>
  </svg>
  <span class="pay-name" style="left:98px;top:3700px;color:#d9412f">Cardora</span>
  <span class="pay-name" style="left:372px;top:3700px;color:#1f6fc9">Paylink</span>
  <span class="pay-name" style="left:646px;top:3700px;color:#444">Tallypass</span>
  <span class="pay-name" style="left:921px;top:3700px;color:#1a3f8f">Veyra</span>
</section>

<section class="reviews2 abs" role="img" aria-label="Photo of a team working together at a table behind a blue overlay"></section>
<h2 class="section-title" style="top:4048px;color:#fff">TESTIMONIALS</h2>
<div class="r2-panel abs"></div>
<div class="bubble" style="left:162px;width:271px">Lorem ipsum dolor sit amet, consectetur adipiscing elit, sed do eiusmod tempor incididunt ut labore et<q>&#8220;</q></div>
<div class="bubble" style="left:460px;width:271px">Lorem ipsum dolor sit amet, consectetur adipiscing elit, sed do eiusmod tempor incididunt ut labore et<q>&#8220;</q></div>
<div class="bubble" style="left:760px;width:277px">Lorem ipsum dolor sit amet, consectetur adipiscing elit, sed do eiusmod tempor incididunt ut labore et<q>&#8220;</q></div>
<div class="r2-who" style="left:170px"><span class="avatar" role="img" aria-label="Reviewer portrait"></span><div>RUTH<br>28 Reviews</div></div>
<div class="r2-who" style="left:468px"><span class="avatar" role="img" aria-label="Reviewer portrait"></span><div>RUTH<br>28 Reviews</div></div>
<div class="r2-who" style="left:768px"><span class="avatar" role="img" aria-label="Reviewer portrait"></span><div>RUTH<br>28 Reviews</div></div>

<footer class="site-footer">
  <div class="brand"><span class="dot"></span>Bright Ledger View</div>
  <div class="socials abs" aria-label="Social links"><span></span><span></span><span></span><span></span></div>
  <div class="fcol" style="left:397px"><h5>NAVIGATION</h5><ul><li>HOME</li><li>ABOUT US</li><li>ARTICLES</li><li>CONTACT US</li></ul></div>
  <div class="fcol" style="left:636px;border-left-color:var(--blue)"><h5>RESOURCES</h5><ul><li>TERMS &amp; CONDITIONS</li><li>PRIVACY POLICY</li><li>DELIVERY PROCESS</li><li>DATA POLICY</li><li>REFUND POLICY</li></ul></div>
  <div class="fcol" style="left:843px;width:260px"><h5>CONTACT INFORMATION</h5>
    <div class="contact-row"><i><svg width="12" height="16" viewBox="0 0 12 16"><path d="M6 15S1 9 1 6a5 5 0 0 1 10 0c0 3-5 9-5 9z" fill="#fff"/><circle cx="6" cy="6" r="2" fill="#8cc63f"/></svg></i>24 HARBOUR LANE,<br>CAPE TOWN 8001</div>
    <div class="contact-row"><i><svg width="14" height="14" viewBox="0 0 14 14"><path d="M3 1l2 3-1.5 1.5a8 8 0 0 0 5 5L10 9l3 2-1 2.5C6 13 1 8 .5 2z" fill="#fff"/></svg></i>+27 21 555 0148</div>
    <div class="contact-row"><i><svg width="14" height="10" viewBox="0 0 14 10"><rect x=".5" y=".5" width="13" height="9" fill="none" stroke="#fff"/><path d="M.5.5l6.5 5 6.5-5" fill="none" stroke="#fff"/></svg></i>HELLO@BRIGHTLEDGERVIEW.CO.ZA</div>
  </div>
  <div class="copy abs">© 2022 BRIGHT LEDGER VIEW ALL RIGHT RESERVED</div>
</footer>

</body>
</html>
```